SOS! The Bramble cafe is in need of a menu face lift!

We need a standout looking menu for our evolving cafe. Our business has grown greatly from our fresh and changing menu, however the menu (look) itself isn't inspiring and is basic.
I have attached some photos of the business and menus I like the look of.
I am open to other ideas (this is why I need your creative help)
Our menu is currently on an A5 clip board, however we are willing to change it a different size if needed.
Updates

Would love to have it a multi function eg, used as a takeaway menu as well, possibly bi-fold? Added Wednesday, June 8, 2016

Industry/Entity Type

Business

Requirements
Nice to have
• It would be cool to have some old sea/ pirate references?

```html
<!DOCTYPE html>
<html lang="en">
<head>
<meta charset="utf-8">
<title>The Bramble – Coffee Bar &amp; Grill Menu</title>
<link href="https://fonts.googleapis.com/css2?family=Montserrat:wght@400;600;700&family=Roboto+Slab:wght@400;700&display=swap" rel="stylesheet">
<style>
:root{
  --navy:#1e5468;
  --navy-deep:#163f4f;
  --teal:#3f8e9b;
  --teal-soft:#cfe3e1;
  --wash:#f4f8f7;
  --ink:#26363b;
  --muted:#5c6c70;
  --ground:#e9eded;
  --photo-warm:#8a5a3a;
  --photo-green:#6f9a55;
}
*{box-sizing:border-box;margin:0;padding:0}
html,body{width:1200px;height:949px;overflow:hidden}
body{background:var(--ground);font-family:"Montserrat",sans-serif;color:var(--ink)}
.sheet{position:absolute;left:21px;width:1158px;height:445px;display:flex;box-shadow:0 2px 8px rgba(0,0,0,.15)}
.sheet--inside{top:20px}
.sheet--outside{top:484px}
.panel{position:relative;width:386px;height:445px;padding:12px 16px;overflow:hidden;
  background:linear-gradient(180deg,var(--teal-soft) 0,var(--wash) 60px,var(--wash) 385px,var(--teal-soft) 445px);
  border-right:1px solid rgba(30,84,104,.12)}
.panel:last-child{border-right:none}
.banner{display:block;margin:4px auto 6px;width:150px;height:24px}
.banner text{font-family:"Roboto Slab",serif;font-weight:700;font-size:13px;letter-spacing:2px;fill:#fff}
.lead{font-family:"Roboto Slab",serif;font-weight:700;font-size:9.5px;text-align:center;line-height:1.25;color:var(--navy);margin:8px 0 8px;text-transform:uppercase}
.subhead{font-weight:700;font-size:9px;color:var(--teal);text-transform:uppercase;margin:5px 0 3px;letter-spacing:.3px}
.item{display:grid;grid-template-columns:1fr auto;column-gap:8px;margin-bottom:4px}
.item__name{font-weight:700;font-size:9px;text-transform:uppercase;color:var(--navy)}
.item__price{font-weight:700;font-size:9px;color:var(--ink)}
.item__desc{grid-column:1/3;font-size:7.3px;line-height:1.25;color:var(--muted)}
.photo{border-radius:3px;border:3px solid #fff;box-shadow:0 1px 3px rgba(0,0,0,.25)}
.photo--breakfast{height:80px;background:linear-gradient(135deg,var(--photo-green),#e2b04a 55%,var(--photo-warm))}
.photo--sides{position:absolute;left:16px;right:16px;bottom:12px;height:64px;background:linear-gradient(90deg,var(--photo-warm),#d9a44c 40%,var(--photo-green) 70%,#c9553d)}
.photo--cup{position:absolute;top:-22px;right:-36px;width:84px;height:84px;border-radius:50%;border:6px solid #fff;background:radial-gradient(circle,#2a1a12 45%,#5a3a28 70%);z-index:2}
.panel--drinks{overflow:visible;z-index:2}
.extras{font-size:7.3px;line-height:1.3;color:var(--muted);margin-top:4px}
.extras b{color:var(--navy);font-size:8.5px;text-transform:uppercase}
.cup-sizes{text-align:center;font-weight:700;font-size:10px;color:var(--navy);margin-bottom:4px}
.brand{text-align:center;margin-top:58px}
.brand__mark{display:inline-block;width:14px;height:14px;border-radius:50%;background:var(--navy);vertical-align:middle;margin-right:8px}
.brand__name{font-family:"Roboto Slab",serif;font-weight:700;font-size:30px;color:var(--navy);vertical-align:middle}
.brand__sub{font-family:"Roboto Slab",serif;font-weight:700;font-size:10px;letter-spacing:3px;color:var(--teal);margin-top:2px}
.photo--cover{height:150px;margin:14px 22px 0;background:linear-gradient(135deg,var(--photo-warm),#c98a44 45%,var(--photo-green) 75%,#e8d7b0)}
.tagline{font-family:"Roboto Slab",serif;font-style:italic;font-size:12px;color:var(--teal);text-align:center;margin:12px 0 8px}
.hours{background:var(--navy);color:#fff;padding:9px 12px;margin:0 6px;font-size:8px;line-height:1.45;text-align:center}
.hours strong{font-size:8.5px;letter-spacing:.5px}
.hours__phone{font-weight:700;font-size:13px;margin:3px 0 1px;display:flex;align-items:center;justify-content:center;gap:6px}
</style>
</head>
<body>

<svg width="0" height="0" style="position:absolute">
  <defs>
    <symbol id="ribbon" viewBox="0 0 150 24">
      <path d="M0 6h14v16H0l5-8z" fill="#163f4f"/>
      <path d="M150 6h-14v16h14l-5-8z" fill="#163f4f"/>
      <rect x="10" y="2" width="130" height="18" fill="#1e5468"/>
    </symbol>
  </defs>
</svg>

<section class="sheet sheet--inside">
  <article class="panel panel--breakfast">
    <div class="photo photo--breakfast" role="img" aria-label="Photo of breakfast plates with eggs, greens and toast"></div>
    <svg class="banner" viewBox="0 0 150 24"><use href="#ribbon"/><text x="75" y="16" text-anchor="middle">BREAKFAST</text></svg>
    <div class="item"><span class="item__name">Toast – served buttered 2 slices</span><span class="item__price">$4.5</span><span class="item__desc">sourdough, white or wholemeal. jam, savoury spread, honey, peanut butter or cinnamon sugar +$0.5</span></div>
    <div class="item"><span class="item__name">GF Bread (2)</span><span class="item__price">$5.5</span></div>
    <div class="item"><span class="item__name">Turkish Raisin (2) Toast</span><span class="item__price">$5.5</span></div>
    <div class="item"><span class="item__name">Banana Bread (GF)</span><span class="item__price">$5.5</span><span class="item__desc">add whipped mascarpone w/ honey +$2.5</span></div>
    <div class="item"><span class="item__name">Granola Muesli</span><span class="item__price">$10.5</span><span class="item__desc">house made granola w/ yoghurt &amp; our own berry compote</span></div>
    <div class="item"><span class="item__name">Spanish Eggs</span><span class="item__price">$15.5</span><span class="item__desc">two poached eggs in rich tomato &amp; chorizo sauce, topped w/ parmesan, served w/ sourdough</span></div>
    <div class="item"><span class="item__name">Bacon &amp; Eggs</span><span class="item__price">$9.0</span><span class="item__desc">poached, scrambled or fried on sourdough toast</span></div>
    <div class="item"><span class="item__name">Bacon &amp; Egg Sandwich</span><span class="item__price">$9.5</span><span class="item__desc">turkish bread toasted w/ bacon, fried egg &amp; relish</span></div>
    <div class="item"><span class="item__name">Lifestyle Breakfast</span><span class="item__price">$13.5</span><span class="item__desc">wholemeal toast topped w/ spinach, tomato, avocado &amp; poached eggs</span></div>
    <div class="item"><span class="item__name">Eggs Benedict</span><span class="item__price">$16.5</span><span class="item__desc">toasted sourdough w/ baby spinach, poached eggs &amp; hollandaise</span></div>
    <div class="item"><span class="item__name">The Big Bramble Breakfast</span><span class="item__price">$19.5</span><span class="item__desc">eggs your way, bacon, sausage, hash brown, tomato, mushrooms &amp; toast</span></div>
  </article>

  <article class="panel panel--breakfast-more">
    <div class="item"><span class="item__name">French Toast</span><span class="item__price">$15.5</span><span class="item__desc">brioche bread soaked in a creamy cinnamon mix, fried &amp; served w/ maple syrup, vanilla ice cream &amp; berries</span></div>
    <div class="item"><span class="item__name">Pancakes</span><span class="item__price">$12.5</span><span class="item__desc">two stack of pancakes, topped w/ maple syrup &amp; ice cream</span></div>
    <div class="item"><span class="item__name">Breakfast Wrap</span><span class="item__price">$13.5</span><span class="item__desc">bacon, fried egg, spinach, cheese topped with house made relish</span></div>
    <div class="item"><span class="item__name">Croissants</span><span class="item__price">$8.5</span><span class="item__desc">ham, cheese &amp; tomato, ham, cheese &amp; avocado</span></div>
    <div class="subhead">Kids Suggestions Breakfast</div>
    <div class="item"><span class="item__name">Egg on Toast</span><span class="item__price">$5.5</span><span class="item__desc">poached / scrambled or fried</span></div>
    <div class="item"><span class="item__name">Mini Bacon &amp; Egg on Toast</span><span class="item__price">$7.5</span></div>
    <div class="item"><span class="item__name">Single Pancake</span><span class="item__price">$6.0</span><span class="item__desc">w/ maple syrup and ice cream</span></div>
    <div class="item"><span class="item__name">Savoury Spread &amp; Cheese Melt</span><span class="item__price">$5.5</span></div>
    <div class="item"><span class="item__name">Mini Ben</span><span class="item__price">$10.5</span><span class="item__desc">1pc sourdough w/ spinach, ham, poached egg &amp; hollandaise</span></div>
    <div class="item"><span class="item__name">Yoghurt</span><span class="item__price">$4.5</span><span class="item__desc">served w/ our berry compote</span></div>
    <p class="extras"><b>Extra's / Sides</b><br>$4 ea bacon (2) · egg (2) · chorizo · salmon · mushrooms. $2 ea grilled tomato · baby spinach · avocado · hash brown. Most items can be made gluten free +$1.5</p>
    <div class="photo photo--sides" role="img" aria-label="Photo strip of side dishes, chips and salads"></div>
  </article>

  <article class="panel panel--lunch">
    <svg class="banner" viewBox="0 0 150 24"><use href="#ribbon"/><text x="75" y="16" text-anchor="middle">LUNCH</text></svg>
    <p class="lead">Wraps lightly toasted &amp; served w/<br>beer battered chips</p>
    <div class="item"><span class="item__name">Chicken Wrap</span><span class="item__price">$15.5</span><span class="item__desc">w/ bacon, mixed lettuce, tasty cheese &amp; your choice of sauce</span></div>
    <div class="item"><span class="item__name">Bramble Wrap</span><span class="item__price">$15.5</span><span class="item__desc">mixed lettuce, sundried tomato, grilled bacon, egg &amp; cheese</span></div>
    <div class="item"><span class="item__name">Vegie Wrap</span><span class="item__price">$15.5</span><span class="item__desc">grilled mushrooms, capsicum, onion, tomato, feta &amp; spinach</span></div>
    <div class="item"><span class="item__name">Lentil Wrap</span><span class="item__price">$15.5</span><span class="item__desc">our own lentil patty w/ lettuce, tomato &amp; mango chutney</span></div>
    <div class="item"><span class="item__name">Chicken Fajita</span><span class="item__price">$16.5</span><span class="item__desc">spiced chicken, capsicum, onion, cheese &amp; sour cream</span></div>
    <div class="item"><span class="item__name">Beef Burrito</span><span class="item__price">$16.5</span><span class="item__desc">seasoned mince, brown rice, black beans, lettuce &amp; salsa</span></div>
    <p class="lead">Burgers made on fresh toasted turkish bread<br>&amp; served w/ beer battered chips</p>
    <div class="item"><span class="item__name">B.L.A.T</span><span class="item__price">$14.5</span><span class="item__desc">bacon, mixed lettuce, avocado &amp; tomato</span></div>
    <div class="item"><span class="item__name">Lentil Burger</span><span class="item__price">$15.5</span><span class="item__desc">our own lentil patty, cheese, tomato &amp; relish</span></div>
    <div class="item"><span class="item__name">Schnitzel Burger</span><span class="item__price">$18.5</span><span class="item__desc">house made schnitzel, lettuce, tomato &amp; mayo</span></div>
    <div class="item"><span class="item__name">American Burger</span><span class="item__price">$18.5</span><span class="item__desc">beef patty, cheese, pickles, onion &amp; mustard</span></div>
    <div class="item"><span class="item__name">Grilled Chicken Burger</span><span class="item__price">$18.5</span><span class="item__desc">grilled chicken breast, bacon, lettuce &amp; aioli</span></div>
  </article>
</section>

<section class="sheet sheet--outside">
  <article class="panel panel--lunch-more">
    <svg class="banner" viewBox="0 0 150 24"><use href="#ribbon"/><text x="75" y="16" text-anchor="middle">LUNCH</text></svg>
    <p class="lead">House made chicken schnitzels – all schnitzels are prepared freshly in house &amp; served w/ a side salad &amp; beer battered chips</p>
    <div class="item"><span class="item__name">Housemade Schnitzel</span><span class="item__price">$19.5</span><span class="item__desc">w/ your choice of mushroom, pepper or plain gravy</span></div>
    <div class="item"><span class="item__name">Chicken &amp; Avocado Schnitzel</span><span class="item__price">$23.5</span><span class="item__desc">topped w/ fresh avocado &amp; cheese grilled</span></div>
    <div class="item"><span class="item__name">Parma Schnitzel</span><span class="item__price">$23.5</span><span class="item__desc">topped w/ our tomato sauce, ham &amp; grilled cheese</span></div>
    <div class="item"><span class="item__name">Hawaiian Schnitzel</span><span class="item__price">$23.5</span><span class="item__desc">topped w/ ham, pineapple &amp; tasty cheese</span></div>
    <div class="subhead">Kids Suggestions Lunch</div>
    <div class="item"><span class="item__name">Nuggets &amp; Chips</span><span class="item__price">$8.0</span></div>
    <div class="item"><span class="item__name">Ham &amp; Pineapple Melt</span><span class="item__price">$6.0</span></div>
    <div class="item"><span class="item__name">Nacho's Corn Chips</span><span class="item__price">$7.5</span><span class="item__desc">topped w/ our salsa, tasty cheese &amp; sour cream</span></div>
    <div class="item"><span class="item__name">Babycino</span><span class="item__price">$1.0</span></div>
    <svg class="banner" viewBox="0 0 150 24"><use href="#ribbon"/><text x="75" y="16" text-anchor="middle">SALADS</text></svg>
    <div class="item"><span class="item__name">Chicken Caesar</span><span class="item__price">$17.5</span><span class="item__desc">grilled chicken, bacon, cos lettuce, croutons, parmesan &amp; a poached egg</span></div>
    <div class="item"><span class="item__name">Prawn &amp; Avocado</span><span class="item__price">$18.5</span><span class="item__desc">lettuce, tomato, cucumber, red onion &amp; seafood dressing</span></div>
    <div class="item"><span class="item__name">Ranch Salad</span><span class="item__price">$18.5</span><span class="item__desc">chicken schnitzel, bacon, mixed leaves, corn &amp; ranch dressing</span></div>
  </article>

  <article class="panel panel--drinks">
    <div class="photo--cup" role="img" aria-label="Photo of a cup of black coffee"></div>
    <svg class="banner" viewBox="0 0 150 24"><use href="#ribbon"/><text x="75" y="16" text-anchor="middle">DRINKS</text></svg>
    <p class="cup-sizes">CUP $3.5 / MUG $4.5 / XL $5.5</p>
    <div class="subhead">Hot Drinks</div>
    <div class="item"><span class="item__name">Espresso</span><span class="item__price">$2.5</span><span class="item__desc">long black / cappuccino / latte / mocha +$0.5 / chocolate / chai / white chocolate / vanilla chai. extras: syrup / honey +$0.5 / soy milk +$0.5</span></div>
    <div class="subhead">Harbour Leaf Teas</div>
    <div class="item"><span class="item__name">2 Cup Pot</span><span class="item__price">$4.5</span><span class="item__desc">english breakfast / earl grey / peppermint / green tea / chai / lemongrass &amp; ginger</span></div>
    <div class="subhead">Cold Drinks</div>
    <div class="item"><span class="item__name">Smoothies</span><span class="item__price">$6.5</span><span class="item__desc">made with fruit, milk, ice cream &amp; yoghurt: mango / mixed berries / banana &amp; honey</span></div>
    <div class="item"><span class="item__name">Tidewater Juices (Bottled)</span><span class="item__price">$4.5</span><span class="item__desc">apple, orange, pineapple, mango &amp; lime, watermelon</span></div>
    <div class="item"><span class="item__name">Milkshake</span><span class="item__price">$5.5</span><span class="item__desc">kids milk shake $3.0 / soy extra $0.5</span></div>
    <div class="item"><span class="item__name">Thickshake</span><span class="item__price">$7.0</span><span class="item__desc">chocolate / vanilla / banana / strawberry / caramel</span></div>
    <div class="item"><span class="item__name">Frappes</span><span class="item__price">$6.0</span><span class="item__desc">your choice of flavour blended w/ milk &amp; ice</span></div>
    <div class="item"><span class="item__name">Traditional Iced Drinks</span><span class="item__price">$6.5</span><span class="item__desc">coffee / mocha / chocolate / chai, served w/ ice cream &amp; cream</span></div>
    <div class="item"><span class="item__name">Cans</span><span class="item__price">$2.5</span><span class="item__desc">cola / diet cola / lemonade / lemon squash</span></div>
    <div class="item"><span class="item__name">Brewer's Bay</span><span class="item__price">$3.5</span><span class="item__desc">ginger beer / lemon, lime &amp; bitters / traditional lemonade</span></div>
  </article>

  <article class="panel panel--cover">
    <div class="brand">
      <span class="brand__mark"></span><span class="brand__name">The Bramble</span>
      <div class="brand__sub">COFFEE BAR &amp; GRILL</div>
    </div>
    <div class="photo photo--cover" role="img" aria-label="Collage of cafe dishes: breakfast plate, cake slice and pastries"></div>
    <p class="tagline">The tastiest breakfast around!</p>
    <div class="hours">
      <strong>BREAKFAST MENU – ALL DAY</strong><br>
      <strong>LUNCH MENU</strong><br>
      MON TO FRI 7.30am • SAT &amp; SUN from 11.30am
      <div class="hours__phone">
        <svg width="12" height="12" viewBox="0 0 24 24" aria-hidden="true"><path fill="#fff" d="M6.6 10.8a15 15 0 0 0 6.6 6.6l2.2-2.2c.3-.3.7-.4 1-.2 1.1.4 2.3.6 3.6.6.6 0 1 .4 1 1V20c0 .6-.4 1-1 1A17 17 0 0 1 3 4c0-.6.4-1 1-1h3.5c.6 0 1 .4 1 1 0 1.3.2 2.5.6 3.6.1.3 0 .7-.2 1z"/></svg>
        +61 2 4000 1234
      </div>
      12 Harbour Rd • Seaview, NSW
    </div>
  </article>
</section>

</body>
</html>
```